LED-Leuchtboxen
Zielgruppe
Wir sind ein Ingenieurbüro und bieten Beratungsdienstleistungen an. Thema ist z.B. Sicherheit in öffentlichen Verwaltungen, Sicherheit von Mitarbeitern am Arbeitsplatz.
L+M Ingenieurgesellschaft für Einsatz- und Ablaufplanung mbH
Ahornweg 17
70329 Stuttgart
Telefon 0711 5893 214
E-Mail info @lm-orbitan.com
Web www.lm-orbitan.com
Wir sind auf einer Messe und brauchen dafür zwei auffällige Designs für zwei LED-Leuchtboxen (Lumvor Dash). Die Besucher der Messe sind Mitarbeiter von öffentlichen Verwaltungen.
Aufgabenstellung
Für die beiden LED-Leuchtboxen brauchen wir farbige und auffällige Bilder/Designs, die aber nicht überfüllt sind und die man sich gerne anschaut. z.B. ein gutes Foto was entfernt etwas mit Sicherheit zu tun hat.
1. Box: Auffälliges Bild als Image-Werbung mit Icon, Firmennamen und vielleicht einem knackigen Spruch ('Heute war ich schon Bitch, Arschloch und wurde bedroht!') Beispiele: Siehe bLenza-Bilder im Anhang.
2. Box: Was wir tun.... (Sicherheit in öffentlichen Verwaltungen: - Notfall- und Krisenmanagement, - KRITIS-Bewertungen, - Fachplanung Sicherungstechnik, - Amok-Konzepte). Hier muss kein Foto im Hintergrund.
An die Vorgaben von Lumvor für die Druckdaten und die Maße ist sich unbedingt zu halten!!! Siehe beide Dateien im Anhang

```html
<!DOCTYPE html>
<html lang="de">
<head>
<meta charset="utf-8">
<title>L+M Leuchtbox</title>
<link rel="stylesheet" href="https://fonts.googleapis.com/css2?family=Bebas+Neue&family=Poppins:wght@700&display=swap">
<style>
  :root {
    --page-bg: #e6e6e6;
    --blue-deep: #1f4fb0;
    --blue-mid: #2a5cbc;
    --blue-light: #3b72c6;
    --accent: #f5a623;
    --white: #ffffff;
    --photo-light: #9fc3e6;
    --photo-mid: #6f9fd6;
    --photo-dark: #2f62b8;
  }
  html, body {
    margin: 0;
    width: 1200px;
    height: 1058px;
    overflow: hidden;
    background: var(--page-bg);
  }
  .lightbox {
    position: absolute;
    left: 385px;
    top: 29px;
    width: 430px;
    height: 1000px;
    overflow: hidden;
    background: linear-gradient(100deg, var(--blue-light) 0%, var(--blue-mid) 45%, var(--blue-deep) 100%);
  }
  .backdrop-curve {
    position: absolute;
    inset: 0;
  }
  .company-name {
    position: absolute;
    left: 41px;
    top: 44px;
    margin: 0;
    width: 350px;
    font-family: "Bebas Neue", sans-serif;
    font-weight: 400;
    font-size: 25px;
    line-height: 28px;
    letter-spacing: 0.4px;
    color: var(--white);
  }
  .headline {
    position: absolute;
    left: 40px;
    top: 192px;
    margin: 0;
    font-family: "Bebas Neue", sans-serif;
    font-weight: 400;
    font-size: 58px;
    line-height: 64px;
    color: var(--white);
  }
  .headline .highlight { color: var(--accent); }
  .photo-area {
    position: absolute;
    left: 128px;
    top: 483px;
    width: 302px;
    height: 517px;
    background: radial-gradient(ellipse at 62% 55%, var(--photo-light) 0%, var(--photo-mid) 45%, var(--photo-dark) 100%);
    border-radius: 150px 0 0 0;
    opacity: 0.85;
  }
  .web-address {
    position: absolute;
    left: 52px;
    top: 953px;
    transform: rotate(-90deg);
    transform-origin: 0 0;
    font-family: "Poppins", sans-serif;
    font-weight: 700;
    font-size: 21px;
    color: var(--white);
    white-space: nowrap;
  }
</style>
</head>
<body>
  <div class="lightbox">
    <svg class="backdrop-curve" width="430" height="1000" viewBox="0 0 430 1000" aria-hidden="true">
      <path d="M280 0 C 420 200, 430 500, 260 820 C 200 930, 100 960, 0 980 L0 0 Z" fill="#3a72c8" opacity="0.35"/>
    </svg>

    <p class="company-name">L+M Ingenieurgesellschaft<br>für Einsatz- und Ablaufplanung mbH</p>

    <h1 class="headline">
      Heute war ich<br>
      <span class="highlight">schon Bitch,</span><br>
      <span class="highlight">Arschloch</span> und<br>
      <span class="highlight">wurde bedroht</span>
    </h1>

    <div class="photo-area" role="img" aria-label="Foto: junge Frau in hellblauer Kleidung sitzt mit angezogenen Knien auf dem Boden und wirkt niedergeschlagen"></div>

    <div class="web-address">www.lm-orbitan.com</div>
  </div>
</body>
</html>
```